Professional business cards for real estate development company

I need business cards for my new real estate development company. The company, "KORVA" is a real estate development, investment, and advisory firm with a focus on multifamily, office, and mixed-use projects across primary and secondary markets in the Southeast United States.

Style preference is modern

Industry/Entity Type

Real Estate Development

Contact Information for Business Card

The business cards need to include:
Name
Title
Mailing Address
Phone Number
Web Address

Logo is attached. I would like white to be the primary color with incorporation of the company colors: #232D3A and #B5A451

Font styles to use
Other font styles liked:
• Montserrat, Avenir

Requirements
Must have
• Company Logo. No need to include the company name since the name is in the logo.
Should not have
• No line type designs

```html
<!DOCTYPE html>
<html lang="en">
<head>
<meta charset="utf-8">
<title>Korva Development – Business Cards</title>
<link rel="stylesheet" href="https://fonts.googleapis.com/css2?family=Lato:wght@400;700&display=swap">
<style>
  :root {
    --backdrop: #4e4e4e;
    --navy: #1e2734;
    --navy-ink: #232d3a;
    --paper: #ececec;
    --logo-light: #c4c6c9;
    --text-dark: #1f2733;
    --text-mid: #4a4f57;
    --charcoal: #232323;
    --emboss: #1c2531;
  }
  * { margin: 0; padding: 0; box-sizing: border-box; }
  html, body { width: 963px; height: 1200px; overflow: hidden; }
  body {
    background: var(--backdrop);
    font-family: "Lato", Arial, sans-serif;
    position: relative;
  }
  .card {
    position: absolute;
    left: 233px;
    width: 555px;
    height: 317px;
    overflow: hidden;
  }
  .card--front { top: 221px; background: var(--paper); }
  .card--back { top: 636px; background: var(--charcoal); }

  .brand-panel {
    position: absolute;
    left: 0; top: 0;
    width: 271px; height: 100%;
    background: var(--navy);
    display: flex; align-items: center; justify-content: center;
  }
  .wordmark {
    display: flex; align-items: center; gap: 10px;
    font-weight: 400;
    letter-spacing: 2px;
    line-height: 1;
  }
  .wordmark__square { display: block; background: currentColor; }
  .wordmark--front { color: var(--logo-light); font-size: 34px; }
  .wordmark--front .wordmark__square { width: 16px; height: 16px; }
  .wordmark--back { color: var(--emboss); font-size: 60px; }
  .wordmark--back .wordmark__square { width: 26px; height: 26px; }
  .card--back { display: flex; align-items: center; justify-content: center; }

  .details { position: absolute; left: 301px; top: 74px; color: var(--text-mid); }
  .details__name { font-size: 18px; font-weight: 700; color: var(--text-dark); letter-spacing: 0.5px; line-height: 22px; }
  .details__title { font-size: 13px; line-height: 16px; }
  .details__company { margin-top: 14px; font-size: 14px; color: var(--text-dark); line-height: 18px; }
  .details__address { font-size: 14px; line-height: 18px; }
  .contact { margin-top: 14px; list-style: none; font-size: 14px; line-height: 18px; }
  .contact__item { display: flex; align-items: center; gap: 9px; }
  .contact__icon { width: 10px; height: 10px; fill: var(--text-dark); flex: none; }
</style>
</head>
<body>
  <section class="card card--front" aria-label="Business card front">
    <div class="brand-panel">
      <div class="wordmark wordmark--front"><span class="wordmark__square"></span>KORVA</div>
    </div>
    <div class="details">
      <p class="details__name">DANIEL REYES</p>
      <p class="details__title">President</p>
      <p class="details__company">Korva Developement LLC</p>
      <p class="details__address">4120 Alder Court</p>
      <p class="details__address">Savannah, Georgia 31405</p>
      <ul class="contact">
        <li class="contact__item">
          <svg class="contact__icon" viewBox="0 0 10 10"><path d="M2 0.5 L3.6 2.6 L2.8 3.6 Q4 6 6.4 7.2 L7.4 6.4 L9.5 8 L8.2 9.5 Q2 8.5 0.5 1.8 Z"/></svg>
          555-214-7730
        </li>
        <li class="contact__item">
          <svg class="contact__icon" viewBox="0 0 10 10"><path d="M0 2 H10 V8 H0 Z M0.6 2.4 L5 5.6 L9.4 2.4" stroke="#ececec" stroke-width="0.8"/></svg>
          hello@korvadevelopment.com
        </li>
        <li class="contact__item">
          <svg class="contact__icon" viewBox="0 0 10 10"><circle cx="5" cy="5" r="4.8"/></svg>
          www.korvadevelopment.com
        </li>
      </ul>
    </div>
  </section>

  <section class="card card--back" aria-label="Business card back">
    <div class="wordmark wordmark--back"><span class="wordmark__square"></span>KORVA</div>
  </section>
</body>
</html>
```